ART/CASTING RESIN LABEL

Clear label for bottle of art/casting epoxy. It needs to be fun,artsy,colorful.
My brand is QUILLO RESIN should read ART/CASTING RESIN.
Attached are a couple of my competitors labels for inspiration
Updates

The bottles will be clear . 12 ounce and 6 ounce. I need the purchaser to see that the resin is crystal clear like water so their project turns out crystal clear..

Target Market(s)

DIY -ARTIST-

Font styles to use
Decorative

Requirements
Must have
• Color and fun

```html
<!DOCTYPE html>
<html lang="en">
<head>
<meta charset="utf-8">
<title>Quillo Resin – Art/Casting Resin Label</title>
<link rel="stylesheet" href="https://fonts.googleapis.com/css2?family=Exo+2:wght@400;500;700;800&display=swap">
<style>
  :root {
    --bg: #ffffff;
    --ink: #1f1f1f;
    --purple: #6a4a8c;
    --slash: #e07a2c;
    --lime: #9ccc1a;
    --bubble-sky: #cfe6f7;
    --bubble-sun: #f8f1b8;
    --bubble-peach: #f6dcc4;
    --art-pink: #e4489a;
    --art-teal: #33c3c9;
    --art-violet: #6b3fa0;
    --art-yellow: #f2e11a;
  }
  html, body {
    margin: 0;
    padding: 0;
    width: 900px;
    height: 1200px;
    overflow: hidden;
    background: var(--bg);
  }
  .label {
    position: relative;
    width: 900px;
    height: 1200px;
    font-family: "Exo 2", sans-serif;
    color: var(--ink);
  }
  .brand-name {
    position: absolute;
    left: 322px;
    top: 268px;
    margin: 0;
    font-size: 34px;
    font-weight: 800;
    letter-spacing: 1px;
    color: var(--ink);
    line-height: 1;
  }
  .product-line {
    position: absolute;
    margin: 0;
    writing-mode: vertical-rl;
    transform: rotate(180deg);
    line-height: 1;
    white-space: nowrap;
  }
  .product-line--type {
    left: 306px;
    top: 358px;
    height: 462px;
    font-size: 66px;
    font-weight: 400;
    letter-spacing: 4px;
    color: var(--purple);
  }
  .product-line--type .slash { color: var(--slash); }
  .product-line--name {
    left: 374px;
    top: 362px;
    height: 290px;
    font-size: 72px;
    font-weight: 500;
    letter-spacing: 18px;
    color: var(--lime);
  }
  .bubble-field {
    position: absolute;
    left: 455px;
    top: 430px;
    width: 160px;
    height: 565px;
    border-radius: 80px;
    background: linear-gradient(180deg, var(--bubble-sky), var(--bubble-sun) 40%, var(--bubble-peach) 70%, var(--bubble-sky));
    opacity: 0.7;
  }
  .mascot-art {
    position: absolute;
    left: 376px;
    top: 682px;
    width: 180px;
    height: 330px;
    border-radius: 46% 46% 40% 40% / 30% 30% 45% 45%;
    background: linear-gradient(160deg, var(--art-pink), var(--art-violet) 45%, var(--art-teal) 75%, var(--art-yellow));
  }
  .volume {
    position: absolute;
    left: 318px;
    top: 884px;
    margin: 0;
    font-size: 19px;
    font-weight: 700;
    line-height: 1.1;
    color: var(--ink);
  }
</style>
</head>
<body>
  <main class="label">
    <h1 class="brand-name">QUILLO RESIN</h1>

    <p class="product-line product-line--type">ART<span class="slash">/</span>CASTING</p>
    <p class="product-line product-line--name">RESIN</p>

    <div class="bubble-field" role="img" aria-label="Decorative scatter of coloured bubbles and rings"></div>

    <div class="mascot-art" role="img" aria-label="Colourful geometric illustration of an owl in pink, teal, violet and yellow"></div>

    <p class="volume">8fl.oz<br>236ml</p>
  </main>
</body>
</html>
```